Small CPA firm
Project: Business cards and stationary
Business cards and stationary - Financial Services
Business cards and stationary
Professional
Darren P. Holcomb
Certified Public Accountant
418 Birchmont Lane, 4-120 Mobile, Alabama 36609
dh@dholcombcpa.example
www.dholcombcpa.example
I'd like a professional but creative looking business card and stationary using my logo. For the business card, I think I would like a design with the logo on the top or the left side, with my name and contact information on the bottom (for logo on top) or right hand side (for logo on left). I'd like to use the same primary colors that the logo uses.
For the back of the card, I think I'd like just the logo without the words in an appropriate format.

```html
<!DOCTYPE html>
<html lang="en">
<head>
<meta charset="utf-8">
<title>Darren P. Holcomb CPA LLC — Stationery</title>
<link href="https://fonts.googleapis.com/css2?family=Cinzel:wght@500&family=Open+Sans:wght@400;600&display=swap" rel="stylesheet">
<style>
:root{
  --bg-dark:#2e2f31;
  --bg-mid:#474849;
  --navy:#1e3a5c;
  --blue:#2f6fa8;
  --blue-light:#7fb2dc;
  --sky:#cfe2f2;
  --paper:#ffffff;
  --paper-shade:#eef1f4;
  --grey:#8d949b;
  --grey-light:#c9ced3;
  --ink:#4a5560;
}
*{margin:0;padding:0;box-sizing:border-box}
html,body{width:1200px;height:310px;overflow:hidden}
body{
  position:relative;
  background:radial-gradient(ellipse at 50% 40%,var(--bg-mid),var(--bg-dark) 75%);
  font-family:"Open Sans",Arial,sans-serif;color:var(--ink);
}
.brand-name{font-family:"Cinzel",Georgia,serif;font-weight:500;color:var(--navy);white-space:nowrap}
.mark{display:inline-block;border-radius:50%;background:var(--blue);flex:none}
.lockup{display:flex;align-items:center;gap:4px}
.piece{position:absolute;background:var(--paper);box-shadow:0 2px 6px rgba(0,0,0,.45);overflow:hidden}
.tiny{font-size:4px;line-height:1.4;color:var(--ink);white-space:nowrap}

/* header */
.header{position:absolute;left:14px;top:28px;width:240px}
.header .lockup{gap:6px}
.header .mark{width:20px;height:20px;background:var(--blue-light)}
.header .brand-name{font-size:11.5px;color:var(--sky)}
.header .tagline{font-size:5.5px;letter-spacing:.1em;text-transform:uppercase;color:var(--grey-light);margin:3px 0 0 26px;white-space:nowrap}
.header .set-label{font-size:5px;color:var(--grey);margin:18px 0 0 26px}

/* business cards */
.card{width:120px;height:60px}
.card .lockup{position:absolute;left:6px;top:6px}
.card .mark{width:9px;height:9px}
.card .brand-name{font-size:5px}
.card .details{position:absolute;left:6px;top:22px}
.card .person{font-size:5px;font-weight:600;color:var(--navy);white-space:nowrap}
.card .band{position:absolute;left:0;right:0;bottom:0;height:7px;background:linear-gradient(90deg,var(--navy),var(--blue),var(--blue-light))}
.card-front-a{left:12px;top:118px}
.card-front-b{left:137px;top:118px}
.card-front-b .details{left:auto;right:6px;text-align:right}
.card-back-white{left:12px;top:216px;height:60px;display:flex;align-items:center;justify-content:center}
.card-back-white .mark{width:22px;height:22px;background:var(--navy)}
.card-back-blue{left:137px;top:216px;height:60px;background:radial-gradient(circle at 50% 45%,var(--blue-light),var(--blue) 45%,var(--navy));display:flex;align-items:center;justify-content:center}
.card-back-blue .mark{width:22px;height:22px;background:var(--sky)}

/* letterheads */
.letterhead .lockup{position:absolute;left:12px;top:12px}
.letterhead .mark{width:11px;height:11px}
.letterhead .brand-name{font-size:6px}
.letterhead .contact{position:absolute;right:10px;top:12px;text-align:right}
.letterhead .watermark{position:absolute;left:50%;top:46%;transform:translate(-50%,-50%);border-radius:50%;border:6px solid var(--paper-shade);background:radial-gradient(circle,#f6f8fa,#e6eaee)}
.letterhead .footer{position:absolute;left:0;right:0;bottom:0}
.letterhead .footer-text{position:absolute;left:0;right:0;bottom:4px;text-align:center;color:#fff}
.letterhead-a{left:268px;top:30px;width:200px;height:258px}
.letterhead-a .watermark{width:110px;height:110px}
.letterhead-b{left:484px;top:12px;width:212px;height:288px}
.letterhead-b .watermark{width:120px;height:120px}

/* envelopes */
.envelope{width:230px;height:64px}
.envelope .lockup{position:absolute;left:8px;top:7px}
.envelope .mark{width:10px;height:10px}
.envelope .brand-name{font-size:5.5px}
.envelope .return{position:absolute;left:22px;top:19px}
.envelope .footer{position:absolute;left:0;right:0;bottom:0}
.envelope .footer-text{position:absolute;right:8px;bottom:2px;color:#fff}
.env-front-a{left:718px;top:98px}
.env-front-b{left:718px;top:236px}
.env-back{width:232px;height:66px;background:var(--paper)}
.env-back svg{position:absolute;inset:0}
.env-back-grey{left:960px;top:80px}
.env-back-blue{left:960px;top:152px}
.env-back-white{left:960px;top:228px}
</style>
</head>
<body>

<header class="header">
  <div class="lockup"><span class="mark"></span><span class="brand-name">Darren P. Holcomb CPA LLC</span></div>
  <p class="tagline">Certified Public Accountant</p>
  <p class="set-label">Stationery Set</p>
</header>

<!-- business cards -->
<section class="piece card card-front-a">
  <div class="lockup"><span class="mark"></span><span class="brand-name">Darren P. Holcomb CPA LLC</span></div>
  <div class="details">
    <p class="person">Darren P. Holcomb</p>
    <p class="tiny">Certified Public Accountant<br>418 Birchmont Lane, 4-120<br>dh@dholcombcpa.example</p>
  </div>
  <div class="band"></div>
</section>

<section class="piece card card-front-b">
  <div class="lockup"><span class="mark"></span><span class="brand-name">Darren P. Holcomb CPA LLC</span></div>
  <div class="details">
    <p class="person">Darren P. Holcomb</p>
    <p class="tiny">Mobile, Alabama 36609<br>dh@dholcombcpa.example<br>www.dholcombcpa.example</p>
  </div>
  <div class="band"></div>
</section>

<section class="piece card card-back-white"><span class="mark"></span></section>
<section class="piece card card-back-blue"><span class="mark"></span></section>

<!-- letterheads -->
<section class="piece letterhead letterhead-a">
  <div class="lockup"><span class="mark"></span><span class="brand-name">Darren P. Holcomb CPA LLC</span></div>
  <p class="contact tiny">418 Birchmont Lane, 4-120<br>Mobile, Alabama 36609<br>dh@dholcombcpa.example</p>
  <div class="watermark"></div>
  <svg class="footer" width="200" height="22" viewBox="0 0 200 22" aria-hidden="true">
    <defs><linearGradient id="bandA" x1="0" x2="1"><stop offset="0" stop-color="#1e3a5c"/><stop offset=".6" stop-color="#2f6fa8"/><stop offset="1" stop-color="#7fb2dc"/></linearGradient></defs>
    <path d="M0 10 Q60 2 120 8 T200 4 V22 H0Z" fill="#cfe2f2"/>
    <path d="M0 13 Q70 6 130 11 T200 8 V22 H0Z" fill="url(#bandA)"/>
  </svg>
  <p class="footer-text tiny">www.dholcombcpa.example</p>
</section>

<section class="piece letterhead letterhead-b">
  <div class="lockup"><span class="mark"></span><span class="brand-name">Darren P. Holcomb CPA LLC</span></div>
  <p class="contact tiny">418 Birchmont Lane, 4-120<br>Mobile, Alabama 36609<br>dh@dholcombcpa.example</p>
  <div class="watermark"></div>
  <svg class="footer" width="212" height="22" viewBox="0 0 212 22" aria-hidden="true">
    <defs><linearGradient id="bandB" x1="0" x2="1"><stop offset="0" stop-color="#1e3a5c"/><stop offset=".6" stop-color="#2f6fa8"/><stop offset="1" stop-color="#7fb2dc"/></linearGradient></defs>
    <path d="M0 10 Q60 2 130 8 T212 4 V22 H0Z" fill="#cfe2f2"/>
    <path d="M0 13 Q70 6 140 11 T212 8 V22 H0Z" fill="url(#bandB)"/>
  </svg>
  <p class="footer-text tiny">www.dholcombcpa.example</p>
</section>

<!-- envelope fronts -->
<section class="piece envelope env-front-a">
  <div class="lockup"><span class="mark"></span><span class="brand-name">Darren P. Holcomb CPA LLC</span></div>
  <p class="return tiny">418 Birchmont Lane, 4-120<br>Mobile, Alabama 36609</p>
  <svg class="footer" width="230" height="12" viewBox="0 0 230 12" aria-hidden="true">
    <path d="M0 6 Q80 0 150 5 T230 2 V12 H0Z" fill="#2f6fa8"/>
  </svg>
  <p class="footer-text tiny">www.dholcombcpa.example</p>
</section>

<section class="piece envelope env-front-b">
  <div class="lockup"><span class="mark"></span><span class="brand-name">Darren P. Holcomb CPA LLC</span></div>
  <p class="return tiny">418 Birchmont Lane, 4-120<br>Mobile, Alabama 36609</p>
  <svg class="footer" width="230" height="12" viewBox="0 0 230 12" aria-hidden="true">
    <path d="M0 6 Q80 0 150 5 T230 2 V12 H0Z" fill="#2f6fa8"/>
  </svg>
  <p class="footer-text tiny">www.dholcombcpa.example</p>
</section>

<!-- envelope backs -->
<section class="piece env-back env-back-grey">
  <svg width="232" height="66" viewBox="0 0 232 66" aria-hidden="true">
    <defs><linearGradient id="flapGrey" x1="0" y1="0" x2="0" y2="1"><stop offset="0" stop-color="#5b6066"/><stop offset="1" stop-color="#c9ced3"/></linearGradient></defs>
    <path d="M0 66 L116 30 L232 66Z" fill="#f2f4f6"/>
    <path d="M0 0 H232 L116 40Z" fill="url(#flapGrey)"/>
  </svg>
</section>

<section class="piece env-back env-back-blue">
  <svg width="232" height="66" viewBox="0 0 232 66" aria-hidden="true">
    <defs><linearGradient id="flapBlue" x1="0" y1="0" x2="0" y2="1"><stop offset="0" stop-color="#1e3a5c"/><stop offset="1" stop-color="#7fb2dc"/></linearGradient></defs>
    <path d="M0 66 L116 30 L232 66Z" fill="#f2f4f6"/>
    <path d="M0 0 H232 L116 40Z" fill="url(#flapBlue)"/>
  </svg>
</section>

<section class="piece env-back env-back-white">
  <svg width="232" height="66" viewBox="0 0 232 66" aria-hidden="true">
    <path d="M0 66 L116 30 L232 66" fill="none" stroke="#c9ced3" stroke-width="1"/>
    <path d="M0 0 L116 40 L232 0" fill="#f6f7f9" stroke="#c9ced3" stroke-width="1"/>
  </svg>
</section>

</body>
</html>
```